Ridgemoor Taproom Beer Can Design

Design a beer can for a boutique craft brewery located in Frankston, Victoria, AUS.
We have a focus on producing socially approachable beers in an ambient setting. The beer can design should be sophisticated, simple, recognizable and a little playful. The color pallet should be inviting and not too bold. The design should have identifying features that can be interchanged onto different cans for different beer types. The design must be repeatable for other beer varieties, which will each have a unique color. The can should feature black, white and purple (this should be in interchangeable color). The beer can also needs to have our Ridgemoor Taproom company logo on it, this has been attached to the design brief.

Target Market(s)

The target market is aged 25+ who are social, have some disposable income and appreciate good beer, wine and food.
The beers will also be made for distribution, initially to locally to restaurants and cafés and eventually commercially.
Tourists will also be targeted due to the area the brewhouse is located (Mornington Peninsula, Victoria, AUS).

Industry/Entity Type

Hospitality

Font styles to use
Sans Serif
Script

Colors
6b449b
876aae
b7a5cd
e4daeb
000000
ffffff
959595

Requirements
Must have
• The ‘Ridgemoor Taproom’ logo.
• The colour associated to this beer - purple. This should be the only colour used on the can (along with black/white/gray).
• The company tagline ‘Socially Approachable’.
• The tasting notes text ‘Bright in colour, dry on the palate and thirst quenching in the extreme, wheat and pale malts compliment each other with nuance.’
• Australian beer can requirements as per 'Requirements.png'. EPS and AI files of the requirements have been included.
Nice to have
• The logo text ‘Cecil Grain IPA’ more predominant than the Ridgemoor Taproom logo.
Should not have
• Be busy, simple is best
• Beer related pictures / images
• Bold, masculine lines and fonts
• Requirements.png directly used. Please use the EPS or AI files provided.

```html
<!DOCTYPE html>
<html lang="en">
<head>
<meta charset="utf-8">
<title>Ridgemoor Taproom – Cecil Grain IPA Can Label</title>
<link rel="stylesheet" href="https://fonts.googleapis.com/css2?family=Raleway:wght@300;400;500&family=Oswald:wght@300;500;700&family=Roboto+Condensed:wght@400;700&display=swap">
<style>
  :root {
    --purple: #6b449b;
    --purple-mid: #876aae;
    --purple-light: #b7a5cd;
    --purple-pale: #e4daeb;
    --ink: #2f3339;
    --black: #000000;
    --white: #ffffff;
    --grey: #959595;
    --label: #f1f1f1;
    --backdrop: #ffffff;
  }
  * { box-sizing: border-box; margin: 0; padding: 0; }
  html, body { width: 1200px; height: 999px; overflow: hidden; background: var(--backdrop); }
  .canvas { position: relative; width: 1200px; height: 999px; background: var(--backdrop); }

  .label { position: absolute; top: 185px; height: 665px; overflow: hidden; }
  .label--front { left: 170px; width: 345px; }
  .label--back { left: 630px; width: 370px; }

  .band { position: absolute; left: 0; right: 0; }
  .band--cap { top: 0; height: 110px; background: var(--purple-mid); }
  .band--rule-top { top: 110px; height: 12px; background: var(--purple-light); }
  .band--field { top: 122px; height: 305px; background: var(--label); }
  .band--rule-bottom { top: 427px; height: 15px; background: var(--purple-light); }
  .band--tagline { top: 442px; height: 93px; background: var(--purple); }
  .band--base { top: 535px; height: 130px; background: var(--ink); }

  .brand {
    position: absolute; left: 0; right: 0; text-align: center;
    font-family: "Raleway", sans-serif; font-weight: 400; color: var(--ink);
    letter-spacing: 2px; text-transform: uppercase;
  }
  .label--front .brand { top: 172px; font-size: 17px; }

  .title-frame {
    position: absolute; left: 5px; top: 245px; width: 312px; height: 162px;
    border: 1px solid var(--purple);
  }
  .title-frame::after {
    content: ""; position: absolute; inset: 6px -6px -6px 6px;
    border: 1px solid var(--purple-mid);
  }
  .title {
    position: absolute; left: 0; right: 0; top: 22px; text-align: center;
    font-family: "Raleway", sans-serif; font-weight: 400; font-size: 51px;
    line-height: 58px; color: var(--purple); letter-spacing: 1px;
  }

  .tagline {
    position: absolute; left: 0; right: 0; top: 474px; text-align: center;
    font-family: "Oswald", sans-serif; font-weight: 300; font-size: 27px;
    color: var(--white); letter-spacing: 0.5px;
  }
  .volume, .strength {
    position: absolute; top: 580px; font-family: "Raleway", sans-serif;
    font-size: 15px; color: var(--white);
  }
  .volume { left: 68px; }
  .strength { left: 225px; }

  .ingredients {
    position: absolute; left: 93px; top: 158px;
    font-family: "Roboto Condensed", sans-serif; font-size: 10px; color: var(--black);
  }
  .ingredients strong { display: block; font-size: 11px; font-weight: 700; }

  .marks { position: absolute; left: 97px; top: 202px; width: 240px; height: 62px; }

  .deposit { position: absolute; left: 95px; top: 286px; font-family: "Roboto Condensed", sans-serif; color: var(--black); }
  .deposit__amount { position: absolute; left: 0; top: 0; font-family: "Oswald", sans-serif; font-weight: 500; font-size: 20px; }
  .deposit__terms { position: absolute; left: 42px; top: 2px; width: 140px; font-size: 8px; line-height: 9px; text-transform: uppercase; }
  .back-strength { position: absolute; left: 95px; top: 323px; font-family: "Roboto Condensed", sans-serif; font-size: 10px; color: var(--black); }

  .standard-drinks { position: absolute; left: 272px; top: 288px; width: 90px; height: 135px; }

  .label--back .brand { top: 472px; font-size: 19px; color: var(--white); }
  .back-title {
    position: absolute; right: 12px; top: 548px;
    font-family: "Raleway", sans-serif; font-weight: 400; font-size: 27px;
    color: var(--white); letter-spacing: 0.5px;
  }
</style>
</head>
<body>
<main class="canvas">

  <section class="label label--front" aria-label="Can front">
    <div class="band band--cap"></div>
    <div class="band band--rule-top"></div>
    <div class="band band--field"></div>
    <div class="band band--rule-bottom"></div>
    <div class="band band--tagline"></div>
    <div class="band band--base"></div>

    <p class="brand">Ridgemoor Taproom</p>
    <div class="title-frame">
      <h1 class="title">CECIL<br>GRAIN IPA</h1>
    </div>
    <p class="tagline">SOCIALLY APPROACHABLE</p>
    <p class="volume">355 ml</p>
    <p class="strength">4.7% ABV</p>
  </section>

  <section class="label label--back" aria-label="Can back">
    <div class="band band--cap"></div>
    <div class="band band--rule-top"></div>
    <div class="band band--field"></div>
    <div class="band band--rule-bottom"></div>
    <div class="band band--tagline"></div>
    <div class="band band--base"></div>

    <p class="ingredients"><strong>INGREDIENTS:</strong>Malt, hops.</p>

    <svg class="marks" viewBox="0 0 240 62" aria-label="Compliance marks">
      <rect x="0" y="0" width="60" height="58" rx="3" fill="#3a3d42"/>
      <circle cx="127" cy="29" r="26" fill="none" stroke="#959595" stroke-width="2"/>
      <circle cx="185" cy="31" r="24" fill="#2f3339"/>
      <path d="M210 8 h30 l-2 40 l-13 10 l-13 -10 z" fill="none" stroke="#2f3339" stroke-width="2"/>
    </svg>

    <div class="deposit">
      <span class="deposit__amount">10c</span>
      <span class="deposit__terms">10c refund at collection depots/points in participating state / territory of purchase</span>
    </div>
    <p class="back-strength">4.8% ABV</p>

    <svg class="standard-drinks" viewBox="0 0 90 135" aria-label="1.2 standard drinks, 330ml">
      <text x="9" y="112" transform="rotate(-90 9 112)" font-family="Roboto Condensed, sans-serif" font-weight="700" font-size="13" fill="#000">Standard Drinks</text>
      <path d="M27 2 h60 l-6 108 h-48 z" fill="none" stroke="#000" stroke-width="3"/>
      <path d="M33 10 h48 l-5 94 h-38 z" fill="#2f3339"/>
      <text x="57" y="46" text-anchor="middle" font-family="Roboto Condensed, sans-serif" font-weight="700" font-size="15" fill="#fff">1.2</text>
      <text x="57" y="127" text-anchor="middle" font-family="Roboto Condensed, sans-serif" font-size="10" fill="#000">330ml</text>
    </svg>

    <p class="brand">Ridgemoor Taproom</p>
    <p class="back-title">CECIL GRAIN IPA</p>
  </section>

</main>
</body>
</html>
```